Bravo Glazing

We need a website design for a company based in Texas that specializes in doors and and windows.
Bravo Glazing is a leading window manufacturer of aluminum and vinyl windows, both serving the replacement and new construction markets. Bravo Glazing Inc. was created over 25 years ago when two existing window manufacturers with excellent reputations in their fields - merged. Bravo Glazing offers a complete line conforming to the needs of residential and commercial window markets.
The final design should be something that communicates professionalism and features they're key value propositions.
Example websites we like:
http://layouts.pebblecraft.example/qx/purse/
http://layouts.pebblecraft.example/qx/splashzone/
http://layouts.pebblecraft.example/qx/refit2/
This design should format the existing content to be more visually organized, improve the fonts to clearer and more readable, and make it easier for users to find services.
Brand guide is attached
Website images can be found here: https://share.vaultdrop.example/7kRtQmZxLpWeYb
Target Market(s)
Windows
Number of Pages Required
1 page
Look and feel
Each slider illustrates characteristics of the customer's brand and the style your logo design should communicate.

```html
<!DOCTYPE html>
<html lang="en">
<head>
<meta charset="utf-8">
<title>Bravo Glazing — Windows, Patio Doors and Sunrooms</title>
<link href="https://fonts.googleapis.com/css2?family=Heebo:wght@300;400;500;700&display=swap" rel="stylesheet">
<style>
:root{
  --navy:#27305a;
  --navy-dark:#141a33;
  --red:#a81d3a;
  --red-soft:#e2395b;
  --grey:#8c92a6;
  --grey-light:#b7bccb;
  --line:#e3e6ee;
  --bg-soft:#f3f5fa;
  --white:#ffffff;
}
*{margin:0;padding:0;box-sizing:border-box}
html,body{width:1200px;height:3051px;overflow:hidden}
body{font-family:"Heebo",Arial,sans-serif;color:var(--navy);background:var(--white);position:relative}
.abs{position:absolute}
section{position:absolute;left:0;width:1200px}

/* hero */
.hero{top:0;height:545px;background:linear-gradient(115deg,#0d1226 0%,#1c2440 35%,#3a4560 55%,#8a8f98 70%,#2a3450 85%,#111830 100%)}
.hero-photo{position:absolute;inset:0}
.nav-rule{position:absolute;left:0;top:69px;width:1200px;height:1px;background:rgba(255,255,255,.25)}
.brand{position:absolute;left:53px;top:26px;font-size:30px;font-weight:400;color:var(--white);letter-spacing:-.5px;display:flex;align-items:center;gap:8px}
.brand-dot{width:10px;height:10px;border-radius:50%;background:var(--white)}
.main-nav{position:absolute;left:452px;top:24px;display:flex;gap:44px}
.main-nav a{color:var(--white);font-size:14px;font-weight:500;text-decoration:none;letter-spacing:.3px}
.btn-chat,.btn-service{position:absolute;top:18px;height:31px;border-radius:16px;font-size:13px;display:flex;align-items:center;justify-content:center;gap:6px}
.btn-chat{left:966px;width:67px;border:1.5px solid var(--white);color:var(--white)}
.btn-service{left:1043px;width:120px;background:var(--white);color:var(--navy-dark);font-weight:500}

/* learn bar */
.learn-bar{top:545px;height:29px;background:#f7f8fb;border-bottom:1px solid var(--line)}
.learn-links{position:absolute;left:53px;top:6px;display:flex;gap:20px;font-size:11.5px;color:var(--grey)}
.learn-links b{color:var(--navy);font-weight:500}
.social-mini{position:absolute;right:56px;top:6px;display:flex;gap:22px;align-items:center}
.social-mini span{width:16px;height:16px;border-radius:50%;background:var(--navy)}
.social-mini span.alt{background:var(--red-soft)}

/* intro */
.intro{top:574px;height:168px;text-align:center}
.intro h1{position:absolute;top:16px;width:100%;font-size:21px;font-weight:400;line-height:29px;color:var(--navy)}
.intro p{position:absolute;top:80px;width:100%;font-size:12.5px;color:var(--grey)}
.btn-dealer{position:absolute;left:520px;top:114px;width:160px;height:38px;border:1.5px solid var(--red);border-radius:20px;color:var(--red);font-size:12px;font-weight:700;letter-spacing:.5px;display:flex;align-items:center;justify-content:center;gap:8px}

/* shared section heads */
.eyebrow{font-size:14px;color:var(--grey-light);font-weight:300}
.section-title{font-size:31px;font-weight:400;color:var(--navy)}
.lead{font-size:12.5px;line-height:21px;color:var(--grey)}

/* services */
.services{top:742px;height:676px;background:var(--bg-soft)}
.tab-list{position:absolute;left:53px;top:245px;width:295px}
.tab{position:absolute;left:0;width:295px;height:79px;display:flex;align-items:center;gap:16px;padding-left:13px;font-size:13px;color:var(--grey)}
.tab.active{background:var(--white);color:var(--red);box-shadow:0 2px 10px rgba(39,48,90,.06)}
.tab-thumb{width:47px;height:47px;border-radius:50%;background:linear-gradient(135deg,#c9b896,#6d7280)}
.panel-title{position:absolute;left:415px;top:267px;font-size:21px;font-weight:400}
.panel-text{position:absolute;left:415px;top:320px;width:690px}
.panel-text p{margin-bottom:15px}
.details{position:absolute;left:415px;top:447px;font-size:12.5px;color:var(--red);font-weight:500}
.panel-img{position:absolute;top:497px;width:201px;height:108px}

/* features */
.features{top:1418px;height:632px;text-align:center}
.feature{position:absolute;width:270px;text-align:left}
.feature svg{display:block;margin-bottom:16px}
.feature h3{font-size:17px;font-weight:700;margin-bottom:14px;color:var(--navy-dark)}
.feature p{font-size:12.5px;line-height:21px;color:var(--grey)}

/* testimonials */
.testimonials{top:2050px;height:456px;background:var(--bg-soft)}
.quote-card{position:absolute;top:248px;width:352px;height:173px;background:var(--white);padding:24px 22px 0 22px;display:flex;gap:22px}
.avatar{flex:0 0 48px;height:48px;border-radius:50%;background:linear-gradient(135deg,#d8c2b0,#8a7468)}
.quote-card p{font-size:11.5px;line-height:18px;color:var(--grey);font-style:italic}
.quote-card cite{display:block;margin-top:12px;font-style:normal;font-size:12px;font-weight:500;color:var(--navy-dark)}

/* contact */
.contact{top:2506px;height:382px}
.contact h2{font-size:18px;font-weight:400;position:absolute}
.field{position:absolute;border:1px solid #cfd3de;border-radius:4px;font-size:11.5px;color:var(--grey);padding:9px 14px}
.btn-send{position:absolute;left:53px;top:301px;width:138px;height:33px;border-radius:17px;background:var(--red);color:var(--white);font-size:12px;font-weight:700;letter-spacing:.4px;display:flex;align-items:center;justify-content:center}
.map{position:absolute;left:334px;top:110px;width:533px;height:224px;background:linear-gradient(120deg,#a9d2ee 0%,#b8dbf1 30%,#e9ecdf 45%,#f1eee5 70%,#dfe9d4 100%)}
.info{position:absolute;left:895px;width:255px;font-size:11.5px;line-height:20px;color:var(--grey)}
.info b{color:var(--navy);font-weight:500}
.info .row{margin-top:9px}
.socials{position:absolute;left:895px;display:flex;gap:12px}
.socials span{width:27px;height:27px;border-radius:50%;background:var(--red)}

/* footer */
.site-footer{position:absolute;left:0;top:2888px;width:1200px;height:163px;border-top:3px solid var(--red)}
.foot-nav{position:absolute;left:53px;top:46px;display:flex;gap:24px;align-items:center;font-size:13px;color:var(--navy)}
.foot-rule{position:absolute;left:53px;top:74px;width:1096px;height:1px;background:var(--line)}
.foot-brand{position:absolute;right:51px;top:36px;font-size:27px;color:var(--red);letter-spacing:-.5px}
.foot-links{position:absolute;left:53px;top:89px;display:flex;gap:20px;font-size:11px;color:var(--grey)}
.foot-legal{position:absolute;right:51px;top:89px;display:flex;gap:20px;font-size:11px;color:var(--grey)}
.foot-bar{position:absolute;left:0;bottom:0;width:1200px;height:6px;background:var(--red)}
</style>
</head>
<body>

<section class="hero">
  <div class="hero-photo" role="img" aria-label="Modern apartment building with large windows lit at dusk"></div>
  <div class="nav-rule"></div>
  <div class="brand"><span class="brand-dot"></span>Bravo Glazing</div>
  <nav class="main-nav"><a href="#">VINYL WINDOWS</a><a href="#">ALUMINUM WINDOWS</a></nav>
  <div class="btn-chat">Chat
    <svg width="12" height="11" viewBox="0 0 12 11"><path d="M1 1h10v7H5l-3 2V8H1z" fill="none" stroke="#fff" stroke-width="1.3"/></svg>
  </div>
  <div class="btn-service">Request Service</div>
</section>

<section class="learn-bar">
  <div class="learn-links"><b>Learn More:</b><span>Our Company</span><span>Knowledge Center</span><span>Careers</span><span>Help &amp; Contact</span></div>
  <div class="social-mini"><span></span><span></span><span class="alt"></span>
    <svg width="14" height="14" viewBox="0 0 14 14"><circle cx="6" cy="6" r="4.5" fill="none" stroke="#27305a" stroke-width="1.6"/><path d="M9.5 9.5L13 13" stroke="#27305a" stroke-width="1.6"/></svg>
  </div>
</section>

<section class="intro">
  <h1>Manufacturer of custom made Windows, Patio Doors and Sunrooms<br>Bravo Glazing is an EFFICIENCY PLUS PARTNER.</h1>
  <p>See some of the features below and learn why People trust Bravo Glazing</p>
  <div class="btn-dealer">
    <svg width="13" height="13" viewBox="0 0 14 14"><circle cx="6" cy="6" r="4.5" fill="none" stroke="#a81d3a" stroke-width="1.8"/><path d="M9.5 9.5L13 13" stroke="#a81d3a" stroke-width="1.8"/></svg>
    FIND A DEALER
  </div>
</section>

<section class="services">
  <div class="abs eyebrow" style="left:53px;top:42px">Services</div>
  <h2 class="abs section-title" style="left:53px;top:66px">Our Windows</h2>
  <p class="abs lead" style="left:53px;top:138px;width:420px">Bravo Glazing is a wholesale window and door manufacturer based out of Cedar Hollow, Texas focused on the replacement / remodeling industry</p>

  <div class="tab-list">
    <div class="tab active" style="top:0"><span class="tab-thumb" role="img" aria-label="Residential home thumbnail"></span>Residential</div>
    <div class="tab" style="top:79px"><span class="tab-thumb" role="img" aria-label="Commercial building thumbnail"></span>Commercial</div>
    <div class="tab" style="top:150px"><span class="tab-thumb" role="img" aria-label="Vinyl window thumbnail"></span>Vinyl Series</div>
    <div class="tab" style="top:221px"><span class="tab-thumb" role="img" aria-label="Aluminum window thumbnail"></span>Aluminum Series</div>
    <div class="tab" style="top:292px"><span class="tab-thumb" role="img" aria-label="Specialty window thumbnail"></span>Specialty Products</div>
  </div>

  <h3 class="panel-title">Residential Window</h3>
  <div class="panel-text lead">
    <p>Our ClearCore Aluminum windows offer homeowners the option to enjoy wide open views with the durability and efficiency necessary for today's energy demands.</p>
    <p>Vinyl windows are the material of choice for millions of homeowners, builders and architects worldwide. For years, Bravo Glazing has been setting the standard for high quality energy-efficient windows for the residential market.</p>
  </div>
  <div class="details">Details &nbsp;›</div>
  <div class="panel-img" style="left:415px;background:linear-gradient(135deg,#d9d4cc,#6e6458)" role="img" aria-label="Bright living room with tall windows"></div>
  <div class="panel-img" style="left:653px;background:linear-gradient(135deg,#cfd3c8,#5f6b58)" role="img" aria-label="Hallway with full-height glazing onto a garden"></div>
  <div class="panel-img" style="left:891px;background:linear-gradient(180deg,#5a88c4,#d8dde4 60%,#8a9a84)" role="img" aria-label="Apartment block facade with rows of windows"></div>
</section>

<section class="features">
  <div class="abs eyebrow" style="left:0;width:1200px;top:32px">Features</div>
  <h2 class="abs section-title" style="left:0;width:1200px;top:58px">Why choose us ?</h2>
  <p class="abs lead" style="left:430px;width:340px;top:130px">We have many years of foreign experience on projects for affluent clients. We know, how to provide high quality work.</p>

  <div class="feature" style="left:195px;top:232px">
    <svg width="64" height="56" viewBox="0 0 64 56" fill="none" stroke="#e2395b" stroke-width="2"><rect x="4" y="20" width="30" height="22"/><path d="M34 26h12l8 9v7H34z"/><circle cx="14" cy="46" r="5"/><circle cx="46" cy="46" r="5"/><circle cx="18" cy="11" r="8"/><path d="M18 6v5h4"/></svg>
    <h3>Arrival on time</h3>
    <p>Sed ut perspiciatis unde omnis iste natus error sit voluptate accusantium doloremqu.</p>
  </div>
  <div class="feature" style="left:475px;top:232px">
    <svg width="64" height="56" viewBox="0 0 64 56" fill="none" stroke="#e2395b" stroke-width="2"><path d="M10 46L38 18M34 8a9 9 0 0 0 12 12l-4-4z"/><path d="M14 8l30 30M40 34l8 8-4 4-8-8z"/></svg>
    <h3>Professional equipment</h3>
    <p>Nemo qui enim ipsam voluptatem quia voluptas sit aspernatur aut odit aut fugit.</p>
  </div>
  <div class="feature" style="left:757px;top:232px">
    <svg width="64" height="56" viewBox="0 0 64 56" fill="none" stroke="#e2395b" stroke-width="2"><path d="M18 8h22l8 9-19 20-19-20z"/><path d="M10 17h38M24 8l5 29 5-29"/><path d="M6 40c6 0 10 8 16 8h16"/><path d="M52 40c-6 0-10 8-16 8"/></svg>
    <h3>Proposition of best solution</h3>
    <p>Sed ut perspiciatis unde omnis iste natus error sit voluptatem accusantium quido et.</p>
  </div>

  <div class="feature" style="left:195px;top:430px">
    <svg width="64" height="56" viewBox="0 0 64 56" fill="none" stroke="#e2395b" stroke-width="2"><path d="M4 28c8-12 18-16 26-16s18 4 26 16c-8 12-18 16-26 16S12 40 4 28z"/><circle cx="30" cy="28" r="8"/><circle cx="30" cy="28" r="3" fill="#e2395b"/></svg>
    <h3>Great sense for detail</h3>
    <p>Sed ut perspiciatis unde omnis iste natus error sit voluptate accusantium doloremqu.</p>
  </div>
  <div class="feature" style="left:475px;top:430px">
    <svg width="64" height="56" viewBox="0 0 64 56" fill="none" stroke="#e2395b" stroke-width="2"><circle cx="28" cy="26" r="18"/><path d="M28 16l3 7h7l-6 4 2 7-6-4-6 4 2-7-6-4h7z"/><path d="M6 26h-4M54 26h-4"/></svg>
    <h3>Professional approach</h3>
    <p>Nemo qui enim ipsam voluptatem quia voluptas sit aspernatur aut odit aut fugit.</p>
  </div>
  <div class="feature" style="left:757px;top:430px">
    <svg width="64" height="56" viewBox="0 0 64 56" fill="none" stroke="#e2395b" stroke-width="2"><rect x="12" y="6" width="30" height="42"/><path d="M6 12v42h30"/><path d="M18 16h18M18 24h18M18 32h18M18 40h10"/></svg>
    <h3>Compliance of your plans</h3>
    <p>Sed ut perspiciatis unde omnis iste natus error sit voluptatem accusantium quido et.</p>
  </div>
</section>

<section class="testimonials">
  <div class="abs eyebrow" style="left:53px;top:48px">Testimonials</div>
  <h2 class="abs section-title" style="left:53px;top:72px">What our clients says ?</h2>
  <p class="abs lead" style="left:53px;top:144px;width:350px">What your clients say about our services and how we helped us and make them life better than before</p>

  <div class="quote-card" style="left:53px">
    <span class="avatar" role="img" aria-label="Client portrait"></span>
    <div><p>Duis aute irure dolor in reprehenderit in voluptate velit esse cillum dolore eu fugiat nulla pariatur. Excepteur sint occaecat cupidatat non proident, sunt in culpa qui officia deserunt mollit.</p><cite>Owen Hartley, Operations Manager</cite></div>
  </div>
  <div class="quote-card" style="left:424px">
    <span class="avatar" role="img" aria-label="Client portrait"></span>
    <div><p>Provident, similique sunt in culpa qui officia deserunt mollitia animi, id est laborum et dolorum fuga. Et harum quidem rerum facilis est et expedita distinctio. Nam libero tempore, cum soluta nobis.</p><cite>Nora Vance, Creative Designer</cite></div>
  </div>
  <div class="quote-card" style="left:794px">
    <span class="avatar" role="img" aria-label="Client portrait"></span>
    <div><p>Luis aute irure dolor in reprehenderit in piluptate velit esse cillum dolore eu fugiat nulla pariatur. Excepteur sint occaecat cupidatat non proident, sunt in culpa qui officia deserunt mollit.</p><cite>Clara Denholm, Manager</cite></div>
  </div>
</section>

<section class="contact">
  <h2 style="left:53px;top:70px">Feel Free to Mail</h2>
  <div class="field" style="left:53px;top:110px;width:116px;height:33px">Name *</div>
  <div class="field" style="left:187px;top:110px;width:118px;height:33px">Email *</div>
  <div class="field" style="left:53px;top:163px;width:252px;height:31px">Subject</div>
  <div class="field" style="left:53px;top:214px;width:252px;height:67px">Write Your Message Here...</div>
  <div class="btn-send">SEND MESSAGE</div>

  <h2 style="left:334px;width:533px;top:74px;text-align:center">Headquarters</h2>
  <div class="map" role="img" aria-label="Street map of the headquarters neighbourhood with a location pin"></div>

  <h2 style="left:895px;top:70px">Contact Info</h2>
  <div class="info" style="top:106px">
    <div>Our staff is available to you from 9AM until 5PM on weekdays.</div>
    <div class="row"><b>Phone:</b> +1 (800) 555 01 42</div>
    <div class="row"><b>Office:</b> 410 Harbor Row, Cedar Hollow</div>
    <div class="row"><b>Email:</b> info@bravoglazing.example</div>
  </div>
  <h2 style="left:895px;top:266px">Follow Us on</h2>
  <div class="socials" style="top:306px"><span></span><span></span><span></span><span></span><span></span></div>
</section>

<footer class="site-footer">
  <div class="foot-nav">
    <svg width="14" height="14" viewBox="0 0 14 14"><circle cx="6" cy="6" r="4.5" fill="none" stroke="#27305a" stroke-width="1.6"/><path d="M9.5 9.5L13 13" stroke="#27305a" stroke-width="1.6"/></svg>
    <span>Help &amp; Contact</span><span>Vinyl Windows</span><span>Aluminum Windows</span><span>Request a Quote</span>
  </div>
  <div class="foot-brand">Bravo Glazing</div>
  <div class="foot-rule"></div>
  <div class="foot-links"><span>Our Company</span><span>Blog</span><span>Careers</span><span>Public Policy</span><span>Sitemap</span><span>Our Community</span><span>Partners</span></div>
  <div class="foot-legal"><span>© 1993 - 2018</span><span>Privacy</span><span>Legal</span><span>Feedback</span></div>
  <div class="foot-bar"></div>
</footer>

</body>
</html>
```